The Red Ember Masa Kitchen

I would like your designers to design a clean business card with information I provide for my business , website is theredembermasakitchen.example and the email is rlpadilla14@mailbox.example , I would like for you to use the two tamales I send, that is my logo if you can fix it up that would be great, I am also open to any other options that you can come up with , thank you

```html
<!DOCTYPE html>
<html lang="en">
<head>
<meta charset="utf-8">
<title>The Red Ember Masa Kitchen — Business Card</title>
<link rel="stylesheet" href="https://fonts.googleapis.com/css2?family=Italianno&family=Arimo:wght@400&display=swap">
<style>
  :root {
    --backdrop: #ece7e1;
    --card-white: #ffffff;
    --sun-yellow: #f8a51d;
    --ember-orange: #f07a22;
    --ember-red: #e1262b;
    --title-brown: #b5561d;
    --text-red: #d8401d;
    --mascot-light: #f6a04a;
    --mascot-mid: #e9772a;
    --mascot-deep: #c44d1b;
  }
  * { box-sizing: border-box; margin: 0; padding: 0; }
  html, body { width: 1200px; height: 800px; overflow: hidden; }
  body {
    position: relative;
    background: var(--backdrop);
    font-family: "Arimo", Arial, sans-serif;
  }
  .card {
    position: absolute;
    left: 451px;
    width: 331px;
    height: 189px;
    overflow: hidden;
    box-shadow: 0 2px 5px rgba(0,0,0,0.25);
  }
  .card-front {
    top: 167px;
    background: linear-gradient(to bottom, var(--sun-yellow) 0%, var(--ember-orange) 45%, var(--ember-red) 100%);
  }
  .front-oval {
    position: absolute;
    left: 42px;
    top: 21px;
    width: 252px;
    height: 142px;
    border-radius: 50%;
    background: rgba(255, 230, 200, 0.35);
  }
  .mascot {
    position: absolute;
    border-radius: 42% 42% 14% 14% / 30% 30% 10% 10%;
    background: linear-gradient(to bottom, var(--mascot-light) 0%, var(--mascot-mid) 55%, var(--mascot-deep) 100%);
  }
  .card-front .mascot { box-shadow: 3px 5px 8px rgba(120, 30, 10, 0.35); }
  .front-mascot-left  { left: 90px;  top: 40px; width: 72px; height: 118px; }
  .front-mascot-right { left: 172px; top: 30px; width: 82px; height: 128px; }
  .card-back {
    top: 393px;
    background: var(--card-white);
  }
  .brand-name {
    position: absolute;
    left: 20px;
    top: 6px;
    font-family: "Italianno", cursive;
    font-weight: 400;
    font-size: 33px;
    line-height: 1;
    color: var(--title-brown);
    white-space: nowrap;
  }
  .language-note {
    position: absolute;
    left: 33px;
    top: 47px;
    font-size: 10.5px;
    color: var(--text-red);
  }
  .back-mascot-left  { left: 36px; top: 85px; width: 54px; height: 74px; }
  .back-mascot-right { left: 97px; top: 73px; width: 52px; height: 89px; }
  .contact-list {
    position: absolute;
    left: 160px;
    top: 80px;
    list-style: none;
    font-size: 10.5px;
    line-height: 19.3px;
    color: var(--text-red);
    white-space: nowrap;
  }
  .back-band {
    position: absolute;
    left: 0;
    bottom: 0;
    width: 100%;
    height: 19px;
    background: linear-gradient(to bottom, #fbd6a8 0%, var(--ember-orange) 30%, var(--ember-red) 100%);
  }
</style>
</head>
<body>
  <section class="card card-front" aria-label="Card front">
    <div class="front-oval"></div>
    <div class="mascot front-mascot-left" role="img" aria-label="Cartoon tamale mascot with moustache and neckerchief, part of the business logo"></div>
    <div class="mascot front-mascot-right" role="img" aria-label="Cartoon tamale mascot with headband, part of the business logo"></div>
  </section>

  <section class="card card-back" aria-label="Card back">
    <h1 class="brand-name">The Red Ember Masa Kitchen</h1>
    <p class="language-note">(Se Habla Espanol)</p>
    <div class="mascot back-mascot-left" role="img" aria-label="Cartoon tamale mascot with moustache, part of the business logo"></div>
    <div class="mascot back-mascot-right" role="img" aria-label="Cartoon tamale mascot with headband, part of the business logo"></div>
    <ul class="contact-list">
      <li>281.555.0147</li>
      <li>713.555.0182</li>
      <li>rlpadilla14@mailbox.example</li>
      <li>theredembermasakitchen.example</li>
    </ul>
    <div class="back-band"></div>
  </section>
</body>
</html>
```